Business Card Design Project

Prime Swift Tasks- http:primeswifttasks.com./janetcorley

Industry/Entity Type

Business

Contact Information for Business Card

Well it could be a pretty color like a glossy pink look business type very Job related

```html
<!DOCTYPE html>
<html lang="en">
<head>
<meta charset="utf-8">
<title>Janet Corley – Business Card</title>
<link href="https://fonts.googleapis.com/css2?family=Exo+2:wght@300;400;500&display=swap" rel="stylesheet">
<style>
  :root {
    --backdrop: #2b2421;
    --card-white: #f7f7f5;
    --accent: #f2a91d;
    --ink: #2a2a2a;
    --rule: #3a3a3a;
    --silver: #e4e6e8;
    --shadow: rgba(0,0,0,0.45);
  }
  * { margin: 0; padding: 0; box-sizing: border-box; }
  html, body {
    width: 1200px; height: 844px; overflow: hidden;
    background: var(--backdrop);
    font-family: "Exo 2", sans-serif;
  }
  .stage {
    position: relative; width: 1200px; height: 844px;
  }
  .card {
    position: absolute; top: 262px;
    width: 540px; height: 320px;
    box-shadow: 0 14px 30px var(--shadow);
  }
  .card--front { left: 50px; background: var(--card-white); color: var(--ink); }
  .card--back { left: 610px; background: var(--accent); }

  .brand {
    position: absolute; right: 36px; top: 36px;
    display: flex; align-items: center; gap: 10px;
    color: var(--accent); font-weight: 500; font-size: 20px;
  }
  .brand__square {
    width: 22px; height: 22px; border: 3px solid var(--accent);
  }
  .holder-name {
    position: absolute; right: 36px; top: 82px;
    font-weight: 300; font-size: 40px; letter-spacing: 0.5px; color: var(--ink);
  }
  .rule {
    position: absolute; left: 36px; right: 36px; height: 1px; background: var(--rule);
  }
  .rule--top { top: 146px; }
  .rule--bottom { top: 254px; }
  .contact-name {
    position: absolute; left: 36px; top: 166px;
    color: var(--accent); font-size: 20px; font-weight: 400; letter-spacing: 0.5px;
  }
  .contact-line {
    position: absolute; left: 36px; top: 204px;
    font-size: 13px; color: var(--ink); white-space: nowrap;
  }
  .contact-line .label { color: var(--accent); }
  .contact-line .sep { color: #888; margin: 0 6px; }
  .contact-line .web { color: var(--accent); }
  .follow {
    position: absolute; left: 36px; top: 272px;
    display: flex; align-items: center; gap: 8px;
    font-size: 14px; letter-spacing: 1px; color: var(--ink);
  }
  .follow__dot {
    width: 22px; height: 22px; background: var(--accent);
  }
  .follow__label { margin-right: 8px; }

  .back-brand {
    position: absolute; inset: 0;
    display: flex; align-items: center; justify-content: center; gap: 14px;
    color: var(--silver); font-size: 28px; font-weight: 500;
  }
  .back-brand__square {
    width: 34px; height: 34px; border: 4px solid var(--silver);
  }
</style>
</head>
<body>
<main class="stage">
  <section class="card card--front">
    <div class="brand"><span class="brand__square"></span><span>Prime Swift Tasks</span></div>
    <h1 class="holder-name">Janet Corley</h1>
    <div class="rule rule--top"></div>
    <p class="contact-name">JANET CORLEY</p>
    <p class="contact-line">
      <span class="label">P:</span> 823-555-0147<span class="sep">|</span><span class="label">E:</span> info@primeswifttasks.com<span class="sep">|</span><span class="web">www.primeswifttasks.com</span>
    </p>
    <div class="rule rule--bottom"></div>
    <div class="follow">
      <span class="follow__label">FOLLOW US ON</span>
      <span class="follow__dot"></span>
      <span class="follow__dot"></span>
      <span class="follow__dot"></span>
      <span class="follow__dot"></span>
    </div>
  </section>

  <section class="card card--back">
    <div class="back-brand"><span class="back-brand__square"></span><span>Prime Swift Tasks</span></div>
  </section>
</main>
</body>
</html>
```